Business card design needed

I need a business card for my new business.
I make environmentally friendly candles from all natural premium ingredients.
The candles are hand-poured locally in Melbourne, Australia.
I also want my card to match my website www.velmirawicks.com.au (similar colours, font). Can add additional fonts to create more interest...
I want my design to reflect class and simplicity.
Target Market(s)
Target audience 25-50
The candles represent luxury but need to appeal to the environmentally conscious...
Needs to appeal to both men and women. A luxury gift a man would buy for his girlfriend or mother or for his home and for a woman it needs to represent quality...
Industry/Entity Type
Business
Contact Information for Business Card
Velmira Candles
Hand-Poured Eco Soy Candles
Lorraine Quibell - Founder
0438 276 904
www.velmirawicks.com.au
Logo Text
VELMIRA
Logo styles of interest
Wordmark Logo
Look and feel
Each slider illustrates characteristics of the customer's brand and the style your logo design should communicate.

```html
<!DOCTYPE html>
<html lang="en">
<head>
<meta charset="utf-8">
<title>Velmira Candles – Business Card</title>
<link rel="stylesheet" href="https://fonts.googleapis.com/css2?family=Josefin+Slab:wght@400;600&family=Arvo&display=swap">
<style>
  :root {
    --page-bg: #e4e4e4;
    --card-bg: #ffffff;
    --ink: #2b2b2b;
    --ink-soft: #8c8c8c;
    --ink-faint: #bdbdbd;
  }
  * { margin: 0; padding: 0; box-sizing: border-box; }
  html, body {
    width: 1200px;
    height: 1000px;
    overflow: hidden;
    background: var(--page-bg);
  }
  .stage {
    width: 1200px;
    height: 1000px;
    display: flex;
    align-items: center;
    justify-content: center;
  }
  .business-card {
    position: relative;
    width: 900px;
    height: 550px;
    background: var(--card-bg);
    box-shadow: 0 6px 18px rgba(0, 0, 0, 0.12);
  }
  .brand-name {
    position: absolute;
    top: 200px;
    left: 0;
    width: 100%;
    text-align: center;
    font-family: "Josefin Slab", serif;
    font-weight: 400;
    font-size: 50px;
    letter-spacing: 0.12em;
    color: var(--ink);
  }
  .tagline {
    position: absolute;
    top: 320px;
    left: 0;
    width: 100%;
    text-align: center;
    font-family: "Josefin Slab", serif;
    font-weight: 600;
    font-size: 17px;
    letter-spacing: 0.16em;
    color: var(--ink-soft);
  }
  .contact-line {
    position: absolute;
    bottom: 50px;
    left: 0;
    width: 100%;
    text-align: center;
    font-family: "Arvo", serif;
    font-size: 17px;
    color: var(--ink);
    white-space: nowrap;
  }
  .contact-label {
    color: var(--ink-faint);
    font-style: italic;
    margin-left: 10px;
  }
  .contact-label:first-child { margin-left: 0; }
</style>
</head>
<body>
  <main class="stage">
    <section class="business-card">
      <h1 class="brand-name">VELMIRA CANDLES</h1>
      <p class="tagline">HAND-POURED ECO SOY CANDLES</p>
      <p class="contact-line">
        <span class="contact-label">FOUNDER</span> LORRAINE QUIBELL
        <span class="contact-label">PHONE</span> 0438 276 904
        <span class="contact-label">WEB</span> WWW.VELMIRAWICKS.COM.AU
      </p>
    </section>
  </main>
</body>
</html>
```